Radiant Crossing - An Exciting Mission & Book Cover Project

Help me to inspire people to live their best life! This is a mission, not just a design project.
I need a Book Cover designed to keep me inspired on the process of writing my book.
Book Title: Radiant Crossing
Tag Line: Three Simple Steps to get out of your own way, SuperCharge your Life and Step into Purpose!
Author: Marlis Quenby

The three steps are: Ownership, Vision and Action (Not sure if this should be on the front or back of the book cover)

The book is a self-help, motivational book. Personal development.
The cover needs to be strong and capture peoples attention, especially with competing shelf space. I almost see a fire ball of flame or explosion that will grab peoples attention.
My company is The Lantern Institute. I have added the company logo and a few pages of my presentation and topic outline to give an idea.
Maybe: The Lantern Institute logo on back of the cover. website is marlisquenby.com

THOUGHT: People should be able to take a photo of them holding the book cover showing what area of life they want Radiant Crossing in. This is why the front cover must be so visual and powerful that they want to take a photo with it. Ie. Explosion, fire, strong and bold.

Target Market(s)

Anyone who feels stuck and needs to breakthrough and move forward in life.

Industry/Entity Type

Motivation

Font styles to use
Serif
Sans Serif

Colors
ec1f27
f37122
fbed22

Requirements
Must have
• The design must be STRONG, SIMPLE, STAND OUT ON BOOK SHELVES.
Must have an open file to swap the photo and copy out.

Back Cover Page
1) Summary
2) 2-3 testimonials. One sentence.
3) About the Author (maybe with photo)
4) Lantern Institute logo
5) Website: radiantcrossing.com and marlisquenby.com
Nice to have
• If my photo works somewhere that would be great. I will change the photo later.
Added Where's Your Harbor? a nice cover example.
Should not have
• Right now I am writing the summary for the back of the cover. For now use Loreum Ipsum text and 2-3 recommendations. Again, I will get these only later.

```html
<!DOCTYPE html>
<html lang="en">
<head>
<meta charset="utf-8">
<title>Radiant Crossing – Cover Spread</title>
<link rel="stylesheet" href="https://fonts.googleapis.com/css2?family=Heebo:wght@400;500&family=Roboto:wght@400&family=Teko:wght@500;600&family=Montserrat:wght@600&display=swap">
<style>
  :root {
    --page: #ffffff;
    --night: #1c0204;
    --ember: #4a0508;
    --crimson: #8a0a0c;
    --red: #ec1f27;
    --orange: #f37122;
    --flame: #ff6a0d;
    --yellow: #fbed22;
    --white: #ffffff;
    --ink: #1a1a1a;
    --suit: #1d2a4f;
    --shirt: #b9c8e0;
    --outline:
      2px 0 0 var(--white), -2px 0 0 var(--white), 0 2px 0 var(--white), 0 -2px 0 var(--white),
      1.5px 1.5px 0 var(--white), -1.5px 1.5px 0 var(--white), 1.5px -1.5px 0 var(--white), -1.5px -1.5px 0 var(--white);
    --outline-thin:
      1px 0 0 var(--white), -1px 0 0 var(--white), 0 1px 0 var(--white), 0 -1px 0 var(--white);
  }
  * { box-sizing: border-box; margin: 0; padding: 0; }
  html, body { width: 1200px; height: 1200px; overflow: hidden; background: var(--page); }
  .canvas { position: relative; width: 1200px; height: 1200px; }

  .spread {
    position: absolute; left: 51px; top: 231px; width: 1102px; height: 745px;
    background: linear-gradient(180deg, var(--night) 0%, var(--ember) 38%, var(--crimson) 62%, var(--red) 78%);
    overflow: hidden;
  }
  .fire {
    position: absolute; left: 0; right: 0; bottom: 0; height: 330px;
    background: linear-gradient(180deg, rgba(236,31,39,0) 0%, rgba(243,113,34,.75) 35%, rgba(251,200,60,.95) 70%, #fde9a0 100%);
  }
  .fold { position: absolute; top: 0; bottom: 0; width: 1px; background: rgba(255,255,255,.35); }
  .fold--left { left: 524px; }
  .fold--right { left: 577px; }

  /* back cover */
  .back__heading {
    position: absolute; left: 0; width: 524px; top: 45px; text-align: center;
    font: 500 25px/1 "Heebo", sans-serif; color: var(--white);
  }
  .back__summary {
    position: absolute; left: 34px; width: 446px; top: 108px;
    font: 400 12px/21.3px "Roboto", sans-serif; color: var(--white); text-align: justify;
  }
  .back__brand {
    position: absolute; left: 0; width: 524px; top: 612px;
    display: flex; align-items: center; justify-content: center; gap: 8px;
    font: 600 19px/1 "Montserrat", sans-serif; color: var(--ink); letter-spacing: .5px;
  }
  .back__brand-dot { width: 14px; height: 14px; border-radius: 50%; background: var(--orange); }
  .back__site {
    position: absolute; left: 0; width: 524px; top: 694px; text-align: center;
    font: 400 19px/1 "Heebo", sans-serif; color: var(--ink);
  }

  /* spine */
  .spine__title, .spine__author {
    position: absolute; left: 524px; width: 53px; writing-mode: vertical-rl;
    display: flex; align-items: center; font-family: "Teko", sans-serif; text-transform: uppercase;
  }
  .spine__title {
    top: 72px; font-weight: 600; font-size: 40px; line-height: 53px; letter-spacing: .5px;
    background: linear-gradient(90deg, var(--flame), var(--yellow));
    -webkit-background-clip: text; background-clip: text; color: transparent;
  }
  .spine__author {
    top: 492px; font-weight: 600; font-size: 34px; line-height: 53px;
    color: var(--flame); text-shadow: var(--outline-thin);
  }

  /* front cover */
  .front__title {
    position: absolute; left: 577px; width: 525px; top: 78px; text-align: center;
    font: 600 54px/1 "Teko", sans-serif; text-transform: uppercase; letter-spacing: 2px;
    background: linear-gradient(180deg, var(--yellow) 20%, var(--orange) 90%);
    -webkit-background-clip: text; background-clip: text; color: transparent;
  }
  .front__tagline {
    position: absolute; left: 643px; width: 425px; top: 129px;
    font: 400 15px/18.5px "Heebo", sans-serif; color: var(--white); text-align: justify; text-align-last: left;
  }
  .front__portrait {
    position: absolute; left: 727px; top: 241px; width: 238px; height: 376px;
    border-radius: 110px 110px 10px 10px;
    background: linear-gradient(180deg, #5a3a30 0%, var(--shirt) 30%, var(--suit) 55%, #121a33 100%);
  }
  .front__author {
    position: absolute; left: 577px; width: 525px; top: 624px; text-align: center;
    font: 600 78px/1 "Teko", sans-serif; text-transform: uppercase;
    color: var(--flame); text-shadow: var(--outline);
  }
</style>
</head>
<body>
<main class="canvas">
  <section class="spread">
    <div class="fire" role="img" aria-label="Wall of bright orange and yellow flames rising along the bottom of the cover"></div>
    <div class="fold fold--left"></div>
    <div class="fold fold--right"></div>

    <h2 class="back__heading">Ownership, Vision and Action</h2>
    <p class="back__summary">Lorem ipsum dolor sit amet, consectetuer adipiscing elit, sed diam nonummy nibh euismod tincidunt ut laoreet dolore magna aliquam erat volutpat. Ut wisi enim ad minim veniam, quis nostrud exerci tation ullamcorper suscipit lobortis nisl ut aliquip ex ea commodo consequat. Duis autem vel eum iriure dolor in hendrerit in vulputate velit esse molestie consequat, Lorem ipsum dolor sit amet, consectetuer adipiscing elit, sed diam nonummy nibh euismod tincidunt ut laoreet dolore magna aliquam erat volutpat. Ut wisi enim ad minim veniam, quis nostrud exerci tation ullamcorper suscipit lobortis nisl ut aliquip ex ea commodo consequat. Duis autem vel eum iriure dolor in hendrerit in vulputate velit esse molestie consequat,</p>
    <div class="back__brand"><span class="back__brand-dot"></span>THE LANTERN INSTITUTE</div>
    <p class="back__site">www.marlisquenby.com</p>

    <div class="spine__title">Radiant Crossing</div>
    <div class="spine__author">Marlis Quenby</div>

    <h1 class="front__title">Radiant Crossing</h1>
    <p class="front__tagline">Three Simple Steps to get out of your own way, SuperCharge your Life and Step into Purpose!</p>
    <div class="front__portrait" role="img" aria-label="Author portrait: smiling man in a navy blazer and light blue shirt"></div>
    <p class="front__author">Marlis Quenby</p>
  </section>
</main>
</body>
</html>
```